Bootstrap Website for Sports Technology Company

Create Bootstrap compatible, HTML and CSS stylesheet-based design templates for typography, forms, buttons, charts, navigation and other interface components for the www.lumacrest-hub.com website. All designs should be Responsive CSS and Fluid.
We are transitioning www.lumacrest-hub.com from Wordpress to Bootstrap and are looking for a fresh, clean landing page with navigation to other page styles. Official Colors and font are attached. Designer may recommend button styles, menu navigation, header, footer, etc. Please incorporate the graphic elements found on the lumacrest-hub.com website.
Page Styles required:
- Landing Page
- Secondary Landing Page
- Five different Page Styles
- small, medium and large buttons
Designers are encouraged to submit the landing page with navigation. We will comment quickly to help with finalizing the design for final selection.
Industry/Entity Type
It Company
Look and feel
Each slider illustrates characteristics of the customer's brand and the style your logo design should communicate.

```html
<!DOCTYPE html>
<html lang="en">
<head>
<meta charset="utf-8">
<title>Lumacrest – The Clubhouse</title>
<link rel="stylesheet" href="https://fonts.googleapis.com/css2?family=Lato:wght@300;400;700;900&display=swap">
<style>
:root{
  --page:#f4f5f6;
  --header:#ececec;
  --ink:#2c3440;
  --muted:#8b9098;
  --nav:#333a44;
  --nav-active:#1f5f9e;
  --rule:#e1e3e6;
  --green:#6cc02a;
  --green-dark:#4e9a16;
  --blue-dark:#2a74b8;
  --panel:#e3e3e3;
  --panel-line:#c9c9c9;
  --footer:#4b505c;
  --footer-text:#9ea3ad;
  --footer-head:#b7bbc3;
  --icon:#3d4756;
}
*{box-sizing:border-box;margin:0;padding:0}
html,body{width:1200px;height:2288px;overflow:hidden}
body{background:var(--page);font-family:'Lato',sans-serif;color:var(--ink);position:relative}
.abs{position:absolute}

.site-header{left:0;top:0;width:1200px;height:86px;background:linear-gradient(#f6f6f6,var(--header));border-bottom:1px solid #cfd2d6}
.brand{left:110px;top:26px;display:flex;align-items:center;gap:10px;font-size:24px;font-weight:700;color:var(--nav-active)}
.brand-mark{width:30px;height:30px;border-radius:50%;background:#8d9297}
.nav-item{top:32px;font-size:16px;font-weight:700;color:var(--nav)}
.nav-item.active{color:var(--nav-active)}

.hero{left:0;top:86px;width:1200px;height:504px;background:linear-gradient(180deg,#3f86d6 0%,#6ba6df 28%,#8fb7cf 45%,#5d8f4f 62%,#3d6e2a 80%,#4d7345 100%)}
.hero-title{left:585px;top:202px;font-size:39px;font-weight:900;color:#fff;text-shadow:0 2px 3px rgba(0,0,0,.25)}
.hero-sub{left:585px;top:260px;font-size:17px;font-weight:700;color:#fff}
.hero-list{left:585px;top:289px;list-style:none;color:#fff;font-size:15px}
.hero-list li{height:36px;display:flex;align-items:center;gap:10px}
.btn-fan{left:585px;top:423px;width:136px;height:42px;border-radius:6px;background:linear-gradient(var(--green),var(--green-dark));color:#1d3310;font-weight:700;font-size:15px;display:flex;align-items:center;justify-content:center;box-shadow:0 2px 3px rgba(0,0,0,.3)}

.device-art{left:114px;top:112px;width:354px;height:790px;border-radius:52px;background:linear-gradient(135deg,#ffffff,#e4e6e9);border:2px solid #d3d6da;box-shadow:0 10px 24px rgba(0,0,0,.15)}

.about-panel{left:501px;top:629px;width:588px;height:266px;background:var(--panel);border:1px solid var(--panel-line);padding:16px 28px}
.about-panel h2{position:relative;font-size:20px;font-weight:400;color:#333;margin-bottom:2px}
.about-panel p{position:relative;font-size:14px;font-weight:300;line-height:40px;color:#6f7277;width:470px}
.about-figure{right:4px;top:4px;width:110px;height:256px;background:radial-gradient(ellipse 30% 50% at 60% 50%,#b9b9b9,rgba(185,185,185,0))}

.rule{left:98px;width:1003px;height:1px;background:var(--rule)}

.feature{top:1044px;width:300px;text-align:center}
.feature-icon{width:130px;height:130px;margin:0 auto;border:4px solid var(--icon);border-radius:50%;display:flex;align-items:center;justify-content:center}
.feature h3{font-size:20px;font-weight:700;margin-top:24px;color:#222;line-height:24px}
.feature p{font-size:13px;line-height:20px;color:var(--muted);margin-top:3px}
.btn-more{margin:24px auto 0;width:155px;height:43px;border-radius:22px;background:linear-gradient(#54a6e6,var(--blue-dark));color:#fff;font-size:14px;font-weight:700;display:flex;align-items:center;justify-content:center;box-shadow:0 3px 4px rgba(0,0,0,.25)}

.point{top:1497px;width:262px}
.point h3{font-size:20px;font-weight:300;color:#333;margin-bottom:10px}
.point h3 b{font-weight:700}
.point p{font-size:12px;line-height:16px;color:#777}
.point .more{margin-top:16px;font-size:12px;color:#777}
.point .more u{text-decoration:none;border-bottom:1px solid #999}

.section-title{left:110px;top:1740px;font-size:20px;font-weight:300;color:#333}
.section-title b{font-weight:700}
.thumb{top:1785px;width:222px;height:158px;background:#fff;border:1px solid #ddd;padding:5px;box-shadow:0 2px 3px rgba(0,0,0,.1)}
.thumb div{width:100%;height:100%}

.site-footer{left:0;top:2015px;width:1200px;height:273px;background:var(--footer)}
.foot-col{top:2038px;font-size:11.5px;line-height:16px;color:var(--footer-text)}
.foot-col h4{font-size:11.5px;font-weight:700;letter-spacing:.5px;color:var(--footer-head);margin-bottom:16px}
.social{left:899px;top:2040px;display:flex;gap:6px}
.social span{width:33px;height:33px;border-radius:3px;background:#6f7582}
.copyright{left:439px;top:2230px;font-size:11px;color:var(--footer-text)}
</style>
</head>
<body>

<header class="site-header abs"></header>
<div class="brand abs"><span class="brand-mark"></span>Lumacrest</div>
<nav aria-label="Main">
  <span class="nav-item active abs" style="left:771px">Home</span>
  <span class="nav-item abs" style="left:852px">Golf</span>
  <span class="nav-item abs" style="left:920px">Clubhouse</span>
  <span class="nav-item abs" style="left:1034px">Contact</span>
</nav>

<section class="hero abs" role="img" aria-label="Blurred golf course under a blue sky"></section>
<div class="device-art abs" role="img" aria-label="Smartphone showing a line drawing of a golfer swinging beside a golf bag with a sensor"></div>
<h1 class="hero-title abs">Welcome to The Clubhouse</h1>
<p class="hero-sub abs">Become a Lumacrest Fan today! It's Free and you will receive:</p>
<ul class="hero-list abs">
  <li><svg width="14" height="12" viewBox="0 0 14 12"><path d="M1 6l4 4 8-9" fill="none" stroke="#fff" stroke-width="2.5"/></svg>Weekly Lumacrest Golf Tips from our Tour Professional</li>
  <li><svg width="14" height="12" viewBox="0 0 14 12"><path d="M1 6l4 4 8-9" fill="none" stroke="#fff" stroke-width="2.5"/></svg>Periodic Newsletter regarding our latest products</li>
  <li><svg width="14" height="12" viewBox="0 0 14 12"><path d="M1 6l4 4 8-9" fill="none" stroke="#fff" stroke-width="2.5"/></svg>Special Member Discounts!</li>
</ul>
<a class="btn-fan abs">Become a Fan</a>

<section class="about-panel abs">
  <div class="about-figure abs" role="img" aria-label="Silhouette of a golfer putting"></div>
  <h2>Lumacrest Enterprise, LLC</h2>
  <p>Lumacrest™ Enterprise, LLC was established as a limited liability company in the State of Westmoor in 2012. Our principal corporate office is located in Harborview, Westmoor. Our goal for 2013 is to launch our flagship TechTool Lumacrest™ Golf and establish a company with a strong social network to promote Lumacrest's How-To Analytics.</p>
</section>

<div class="rule abs" style="top:987px"></div>

<div class="feature abs" style="left:110px">
  <div class="feature-icon" role="img" aria-label="Golfer silhouette icon"><svg width="60" height="90"><rect x="15" y="5" width="30" height="80" rx="12" fill="var(--icon)"/></svg></div>
  <h3>Collect</h3>
  <p>Lorem ipsum dolor sit amet, consectetur adipiscing elit. Vivamus luctus urna sed urna ultricies ac tempor dui sagittis.</p>
  <a class="btn-more">Read more</a>
</div>
<div class="feature abs" style="left:455px">
  <div class="feature-icon" role="img" aria-label="Microscope icon"><svg width="70" height="80"><rect x="25" y="8" width="20" height="36" rx="4" fill="var(--icon)"/><rect x="10" y="52" width="50" height="8" fill="var(--icon)"/><rect x="5" y="68" width="60" height="8" fill="var(--icon)"/></svg></div>
  <h3>Analyzed</h3>
  <p>Lorem ipsum dolor sit amet, consectetur adipiscing elit. Vivamus luctus urna sed urna ultricies ac tempor dui sagittis.</p>
  <a class="btn-more">Read more</a>
</div>
<div class="feature abs" style="left:788px">
  <div class="feature-icon" role="img" aria-label="Arrows flow icon"><svg width="70" height="70"><path d="M10 5v55h50M25 20h30M25 40h30" fill="none" stroke="var(--icon)" stroke-width="5"/><path d="M52 12l10 8-10 8M52 32l10 8-10 8" fill="none" stroke="var(--icon)" stroke-width="4"/></svg></div>
  <h3>Instruct</h3>
  <p>Lorem ipsum dolor sit amet, consectetur adipiscing elit. Vivamus luctus urna sed urna ultricies ac tempor dui sagittis.</p>
  <a class="btn-more">Read more</a>
</div>

<div class="rule abs" style="top:1431px"></div>

<div class="point abs" style="left:128px">
  <h3>Professional <b>target analyzing</b></h3>
  <p>Phasellus sollicitudin gravida nisl, mollis feugiat metus tincidunt in. Pellentesque id sem convallis urna vehicula imperdiet. Aliquam venenatis commodo malesuada laoreet, pellentesque at mauris erat volutpat.</p>
  <p class="more">Estique <u>dova lormae</u></p>
</div>
<div class="point abs" style="left:467px">
  <h3>Stay focus and <b>reach your goal!</b></h3>
  <p>Nullam sed ante ac magna commodo ullamcorper. Integer sagittis, mauris eget blandit congue, urna lorem pulvinar metus, eu facilisis dui lectus et urna. Donec diam turpis, elementum a congue non, euismod eget lorem.</p>
  <p class="more">Deu malou <u>lelopa</u></p>
</div>
<div class="point abs" style="left:805px">
  <h3>Your data is <b>safe with us</b></h3>
  <p>Pellentesque habitant morbi tristique senectus et netus et malesuada fames ac turpis egestas. Do integer tortor ante, ornare sed dignissim posu ere, aliquam ut est.Vestibulum porta ornare vestibulum.</p>
  <p class="more">Sed vel <u>aliquet es.</u></p>
</div>

<div class="rule abs" style="top:1701px"></div>

<h2 class="section-title abs">Work <b>Process</b></h2>
<div class="thumb abs" style="left:110px"><div role="img" aria-label="Close-up of a dark phone" style="background:linear-gradient(135deg,#3a3f45,#111)"></div></div>
<div class="thumb abs" style="left:362px"><div role="img" aria-label="Fabric and blue leather detail" style="background:linear-gradient(135deg,#2d5a85 0 18%,#c8c0b0 18%,#aca595)"></div></div>
<div class="thumb abs" style="left:615px"><div role="img" aria-label="Pen on a wooden desk" style="background:linear-gradient(135deg,#e9e7e2 0 20%,#1e1e1e 20% 32%,#b8834a 32%,#8a5a2c)"></div></div>
<div class="thumb abs" style="left:867px"><div role="img" aria-label="Screen interface close-up" style="background:linear-gradient(90deg,#e8ecef 0 20%,#9ec6e8 20% 28%,#3b8fd3 28%)"></div></div>

<footer class="site-footer abs"></footer>
<div class="foot-col abs" style="left:110px"><h4>ABOUT</h4>Team Portal<br>Lumacrest Exchange</div>
<div class="foot-col abs" style="left:270px"><h4>WHO WE ARE</h4>About us<br>Our Company<br>Product Development</div>
<div class="foot-col abs" style="left:439px;width:232px"><h4>OUTREACH</h4>Lumacrest Attends Brightpath Leaders Forum 2013<br>Lumacrest Attends Westmoor Venture Summit 2013<br>Ready to Tee Up First of Three Product Launches<br>Lumacrest Attends TechHive Spring 2013</div>
<div class="foot-col abs" style="left:738px"><h4>OTHER INFORMATION</h4>Privacy Policy<br>Terms &amp; Condition</div>
<div class="social abs" aria-label="Social links"><span></span><span></span><span></span><span></span><span></span></div>
<p class="copyright abs">© 2013 All Rights Reserved - Lumacrest Enterprise, LLC</p>

</body>
</html>
```